Letterhead & Business Card for our Professional Practice (Financial Services)

We are looking for someone to design a letterhead and business card for our business, which is a professional practice called Harbor Lumen Capital Limited. The website is at www.harborrlumencapital.example.co.uk.

The letterhead needs to have: (a) our logo (b) address (c) telephone number (d) email address and (e) our company number.

We would like the stationary to be consistent with the website.

I have attached the logo in EPS and PNG format.

Target Market(s)

Professional services, large commercial enterprises, financial services

Industry/Entity Type

Financial Service

Font styles to use
Serif

Colors
3176b5
f04a50

Requirements
Must have
• Be consistent with our website located at www.harborlumencapital.example.co.uk
• Be in the following formats:
• 1. Word template for the letterhead
• 2. PDF for the letterhead with setup and bleeds required at www.presskite.example.co.uk
• 3. PDF for the business card with setup and bleeds required at www.presskite.example.co.uk
Nice to have
• Something with a really interesting design that says "these guys are professional but dynamic and interesting"
Should not have
• Boring

```html
<!DOCTYPE html>
<html lang="en">
<head>
<meta charset="utf-8">
<title>Harbor Lumen Capital – Stationery</title>
<link href="https://fonts.googleapis.com/css2?family=Marcellus&family=Arimo:wght@400;700&display=swap" rel="stylesheet">
<style>
  :root{
    --navy:#0d3a6e;
    --navy-light:#1d5291;
    --red:#d0202f;
    --paper:#ffffff;
    --backdrop:#e9eaec;
    --ink:#333;
  }
  *{box-sizing:border-box;margin:0;padding:0}
  html,body{width:1200px;height:937px;overflow:hidden;background:var(--backdrop)}
  body{position:relative;font-family:"Arimo",Arial,sans-serif;color:var(--ink)}
  .sheet{position:absolute;background:var(--paper);overflow:hidden}
  .rounded{border-radius:8px}
  .wave-band{position:absolute;left:0;bottom:0;width:100%;display:block}
  .brand{display:flex;align-items:center;gap:6px;font-family:"Marcellus",Georgia,serif;color:var(--navy);white-space:nowrap}
  .brand-square{display:inline-block;background:var(--red)}
  .brand.stack{flex-direction:column;gap:4px}

  /* letterhead */
  .letterhead{left:185px;top:66px;width:385px;height:546px}
  .letterhead .brand{position:absolute;left:17px;top:26px;font-size:14px}
  .letterhead .brand-square{width:34px;height:34px}
  .contact-block{position:absolute;right:16px;top:20px;text-align:right;font-style:normal;font-size:4.6px;line-height:8.6px;font-weight:700;color:#444}
  .contact-block .gap{height:3px}
  .letter-body{position:absolute;left:36px;top:137px;width:295px;font-size:5px;line-height:7.2px;color:#555}
  .letter-body p{margin-bottom:9px}
  .letter-body .strong{font-weight:700;color:#333}
  .signature{height:20px;width:40px}
  .signature svg{display:block}

  /* folder */
  .folder{left:636px;top:40px;width:458px;height:576px}
  .folder .brand{position:absolute;left:0;right:0;top:224px;justify-content:center;font-size:27px;gap:8px}
  .folder .brand-square{width:82px;height:82px}

  /* cards */
  .card-front{left:45px;top:665px;width:177px;height:95px}
  .card-front .brand{position:absolute;left:6px;top:8px;font-size:7.5px;gap:3px}
  .card-front .brand-square{width:22px;height:22px}
  .card-person{position:absolute;right:12px;top:40px;text-align:center;font-size:3.6px;line-height:4.6px;color:#555;text-transform:uppercase}
  .card-lines{position:absolute;left:10px;top:41px;font-size:3.4px;line-height:5.2px;color:#555}
  .card-back{left:45px;top:785px;width:177px;height:100px}
  .card-back .brand{position:absolute;left:0;right:0;top:28px;justify-content:center;font-size:8.5px;gap:4px}
  .card-back .brand-square{width:26px;height:26px}

  /* envelopes */
  .envelope-front{left:265px;top:671px;width:434px;height:209px}
  .envelope-front .brand{position:absolute;left:14px;top:22px;font-size:10.5px;gap:4px}
  .envelope-front .brand-square{width:34px;height:34px}
  .envelope-back{left:737px;top:671px;width:374px;height:209px}
  .envelope-flap{position:absolute;left:0;top:0;width:100%;height:72px;background:var(--navy);border-radius:0 0 40px 40px}
</style>
</head>
<body>

<svg width="0" height="0" style="position:absolute" aria-hidden="true">
  <defs>
    <linearGradient id="band-fill" x1="0" y1="0" x2="1" y2="1">
      <stop offset="0" stop-color="#d0202f"/>
      <stop offset="0.35" stop-color="#1d5291"/>
      <stop offset="1" stop-color="#0d3a6e"/>
    </linearGradient>
  </defs>
</svg>

<!-- Letterhead -->
<section class="sheet letterhead" aria-label="Letterhead">
  <div class="brand stack"><span class="brand-square"></span><span class="brand-name">Harbor Lumen Capital</span></div>
  <address class="contact-block">
    12 Quay Street<br>Harbour Road
    <div class="gap"></div>
    012 345 6789<br>012 345 6789<br>012 345 6789<br>
    info@harborlumencapital.example.co.uk<br>
    www.harborlumencapital.example.co.uk
  </address>
  <div class="letter-body">
    <p>July 2, 2012</p>
    <p><span class="strong">Dear Client,</span><br>ABC Building, def St., Country Name</p>
    <p>is simply sample text of the printing and layout trade. This text has been the standard placeholder for many years, used when a printer took a tray of type and arranged it to make a sample book. It has lasted through many changes in the trade and the move into digital layout, remaining largely unchanged. It became common on transfer sheets holding sample passages, and later in desktop layout software including versions of this text.</p>
    <p>is simply sample text of the printing and layout trade. This text has been the standard placeholder for many years, used when a printer took a tray of type and arranged it to make</p>
    <p style="margin-top:16px">is simply sample text of the printing and layout trade. This text has been the standard placeholder for many years, used when a printer took a tray of type and arranged it to make a sample book. It has lasted through many changes in the trade and the move into digital layout, remaining largely unchanged. It became common on transfer sheets holding sample passages, and later in desktop layout software including versions of this text.</p>
    <p>Best Regards,</p>
    <div class="signature"><svg width="40" height="20" viewBox="0 0 40 20"><path d="M3 16 C6 4 9 2 8 14 C12 8 16 10 14 15 C20 10 26 12 36 12" fill="none" stroke="#222" stroke-width="0.8"/></svg></div>
    <p><span class="strong">Daniel Reyes</span><br>Director<br><br>ABC Building, def St., Country Name</p>
  </div>
  <svg class="wave-band" viewBox="0 0 400 150" height="120" preserveAspectRatio="none" role="img" aria-label="Curved colour band in red and navy">
    <path d="M0 80 C130 112 270 100 400 0 L400 150 L0 150Z" fill="url(#band-fill)"/>
  </svg>
</section>

<!-- Presentation folder -->
<section class="sheet folder" aria-label="Presentation folder">
  <div class="brand stack"><span class="brand-square"></span><span class="brand-name">Harbor Lumen Capital</span></div>
  <svg class="wave-band" viewBox="0 0 400 150" height="140" preserveAspectRatio="none" role="img" aria-label="Curved colour band in red and navy">
    <path d="M0 80 C130 112 270 100 400 0 L400 150 L0 150Z" fill="url(#band-fill)"/>
  </svg>
</section>

<!-- Business card front -->
<section class="sheet rounded card-front" aria-label="Business card front">
  <div class="brand"><span class="brand-square"></span><span class="brand-name">Harbor Lumen Capital</span></div>
  <div class="card-person">Owen Carter<br>President</div>
  <div class="card-lines">012 345 6789<br>012 345 6789<br>012 345 6789<br>info@harborlumencapital.example.co.uk<br>www.harborlumencapital.example.co.uk</div>
  <svg class="wave-band" viewBox="0 0 400 150" height="30" preserveAspectRatio="none" role="img" aria-label="Curved colour band in red and navy">
    <path d="M0 80 C130 112 270 100 400 0 L400 150 L0 150Z" fill="url(#band-fill)"/>
  </svg>
</section>

<!-- Business card back -->
<section class="sheet rounded card-back" aria-label="Business card back">
  <div class="brand stack"><span class="brand-square"></span><span class="brand-name">Harbor Lumen Capital</span></div>
</section>

<!-- Envelope front -->
<section class="sheet envelope-front" aria-label="Envelope front">
  <div class="brand stack"><span class="brand-square"></span><span class="brand-name">Harbor Lumen Capital</span></div>
  <svg class="wave-band" viewBox="0 0 400 150" height="115" preserveAspectRatio="none" role="img" aria-label="Curved colour band in red and navy">
    <path d="M0 80 C130 112 270 100 400 0 L400 150 L0 150Z" fill="url(#band-fill)"/>
  </svg>
</section>

<!-- Envelope back -->
<section class="sheet envelope-back" aria-label="Envelope back">
  <div class="envelope-flap"></div>
</section>

</body>
</html>
```